The (Private) News Sharing Report

This is a professional and academic report of 35 pages for journalists and teachers. The topic of the report is News Sharing: journalism, social networks and technology. Attached there is an example of the kind of design we are looking for: visual, fresh and modern.

Target Market(s)

Journalists, Journalism Students, Communication Researchers,

Industry/Entity Type

Media

Font styles to use
Sans Serif

Colors
3276b5
33a6d7
886aae
b868aa

Requirements
Must have
• Copyleft images, visual style
Nice to have
• There is an example attached.

```html
<!DOCTYPE html>
<html lang="en">
<head>
<meta charset="utf-8">
<title>The (Private) News Sharing Report – Research Questions</title>
<link rel="stylesheet" href="https://fonts.googleapis.com/css2?family=Josefin+Sans:wght@300;400&family=Nunito:wght@900&display=swap">
<style>
  :root {
    --brand-blue: #3276b5;
    --ink: #2b2b2b;
    --page-white: #ffffff;
    --wood-light: #e9c9a0;
    --wood-mid: #d9ab78;
    --wood-dark: #c58f5c;
  }
  html, body {
    margin: 0;
    padding: 0;
    width: 1200px;
    height: 849px;
    overflow: hidden;
    background: var(--page-white);
  }
  .spread {
    position: relative;
    width: 1200px;
    height: 849px;
    overflow: hidden;
    font-family: "Josefin Sans", "Century Gothic", sans-serif;
    color: var(--ink);
  }
  .desk-photo {
    position: absolute;
    inset: 0;
    width: 1200px;
    height: 849px;
  }
  .section-title {
    position: absolute;
    left: 854px;
    top: 98px;
    margin: 0;
    font-family: "Nunito", "Futura", sans-serif;
    font-weight: 900;
    font-size: 23px;
    letter-spacing: 0.2px;
    color: var(--brand-blue);
  }
  .intro {
    position: absolute;
    left: 854px;
    top: 171px;
    margin: 0;
    font-weight: 300;
    font-size: 17px;
    line-height: 20px;
  }
  .question {
    position: absolute;
    left: 854px;
    margin: 0;
    font-weight: 300;
    font-size: 17px;
    line-height: 25.2px;
  }
  .question-number {
    position: absolute;
    left: 0;
    top: 0;
  }
  .question-text {
    display: block;
    padding-left: 29px;
  }
  .q1 { top: 235px; }
  .q2 { top: 331px; }
  .q3 { top: 432px; }
  .q4 { top: 533px; }
  .q5 { top: 608px; }
  .q6 { top: 709px; }
  .folio {
    position: absolute;
    top: 810px;
    font-size: 7.5px;
    font-weight: 300;
    color: var(--ink);
  }
  .folio-number {
    font-weight: 400;
    font-size: 8px;
  }
  .folio-left { left: 37px; }
  .folio-left .folio-number { margin-right: 13px; }
  .folio-right { right: 38px; }
  .folio-right .folio-number { margin-left: 13px; }
</style>
</head>
<body>
<div class="spread">
  <svg class="desk-photo" role="img" aria-label="Photograph of a wooden desk with reading glasses, a black pen and an open spiral notebook" viewBox="0 0 1200 849" preserveAspectRatio="none">
    <defs>
      <linearGradient id="wood" x1="0" y1="0" x2="1" y2="0.3">
        <stop offset="0" stop-color="var(--wood-light)"/>
        <stop offset="0.5" stop-color="var(--wood-mid)"/>
        <stop offset="1" stop-color="var(--wood-dark)"/>
      </linearGradient>
    </defs>
    <rect width="1200" height="849" fill="url(#wood)"/>
    <rect x="729" y="47" width="471" height="802" fill="var(--page-white)"/>
  </svg>

  <h2 class="section-title">Research Questions</h2>

  <p class="intro">This report is divided into the following six<br>research questions:</p>

  <p class="question q1"><span class="question-number">1)</span><span class="question-text">How appropriate friendly are private<br>online messaging networks for<br>journalism?</span></p>
  <p class="question q2"><span class="question-number">2)</span><span class="question-text">Can private messaging be useful for<br>building trust between the media/<br>journalists and communities?</span></p>
  <p class="question q3"><span class="question-number">3)</span><span class="question-text">How can journalists use private<br>channels/platforms to be part of a<br>community?</span></p>
  <p class="question q4"><span class="question-number">4)</span><span class="question-text">What are the new skills that the media<br>landscape is requiring of journalists?</span></p>
  <p class="question q5"><span class="question-number">5)</span><span class="question-text">What do we know about the<br>audience that is using private<br>messaging for News Sharing?</span></p>
  <p class="question q6"><span class="question-number">6)</span><span class="question-text">What are the best media practices<br>with private online<br>messaging?</span></p>

  <div class="folio folio-left"><span class="folio-number">6</span>The (Private) News Sharing Report</div>
  <div class="folio folio-right">The (Private) News Sharing Report<span class="folio-number">7</span></div>
</div>
</body>
</html>
```